Web App, Website for Heavy Truck Roadside Assistance

We need a website designed called tolbrix.com The main aim of Tolbrix is to offer On Demand Roadside Assistance to heavy trucks/18 wheeler's in USA. I have attached the contents, with detailed instructions. The site needs to be very inviting and bright with some small colors, that would be eye popping to the viewer. I would also like to add header slider.. here is a demo of the old site... (this is just for reference ONLY) http://tolbrix.samplehost.net/app_dev.php/#!portfolio. Add photos as needed

Target Market(s)

Heavy Truck Roadside Assistance

Number of Pages Required

1 page

Font styles to use
Serif

Requirements
Must have
• sample link in the Project description
Nice to have
• use your own ideals

```html
<!DOCTYPE html>
<html lang="en">
<head>
<meta charset="utf-8">
<title>Tolbrix – Roadside Assistance in the USA</title>
<link rel="stylesheet" href="https://fonts.googleapis.com/css2?family=Montserrat:wght@300;400;600;700;800&family=Raleway:wght@400;500&display=swap">
<style>
:root{
  --red:#e5305a;
  --red-dark:#cf2048;
  --ink:#222;
  --muted:#6c6c6c;
  --light:#a2a2a2;
  --white:#fff;
}
*{margin:0;padding:0;box-sizing:border-box}
html,body{width:1200px;height:3571px;overflow:hidden;background:var(--white)}
body{position:relative;font-family:"Raleway",sans-serif;color:var(--ink)}
.abs{position:absolute}

/* hero */
.hero{left:0;top:0;width:1200px;height:720px;overflow:hidden}
.hero-photo{position:absolute;inset:0;background:linear-gradient(180deg,#d7b1b8 0%,#a98d86 30%,#6d7460 60%,#6f6f6c 85%,#8d8b86 100%)}
.hero-curve{position:absolute;left:0;bottom:0}
.brand{left:0;width:1200px;top:72px;font-family:"Montserrat",sans-serif;font-weight:800;font-size:64px;letter-spacing:2px;color:#1d1d1d;text-align:center}
.hero-title{left:0;width:1200px;top:296px;font-family:"Montserrat",sans-serif;font-weight:700;font-size:43px;letter-spacing:1px;color:var(--white);text-align:center}
.hero-sub{left:0;width:1200px;top:360px;font-size:14px;color:#f3f3f3;text-align:center}
.play{left:564px;top:394px}

/* headings */
.section-title{left:0;width:1200px;font-family:"Montserrat",sans-serif;font-weight:300;font-size:44px;text-align:center}
.section-title .accent{color:var(--red)}
.about-title{top:718px;color:var(--red)}
.about-text{left:148px;width:904px;top:790px;font-size:14px;line-height:26px;color:var(--muted);text-align:center}

.feature{width:320px;text-align:center}
.feature svg{display:block;margin:0 auto}
.feature h3{margin-top:22px;font-family:"Montserrat",sans-serif;font-weight:400;font-size:24px;letter-spacing:.5px;color:var(--ink)}
.feature p{margin:10px auto 0;width:280px;font-size:14px;line-height:20px;color:var(--muted)}
.btn-outline{display:inline-block;border:1.5px solid var(--red);color:var(--red);font-family:"Montserrat",sans-serif;font-size:15px;text-align:center}
.feature .btn-outline{margin-top:22px;width:152px;height:42px;line-height:40px}

/* how it works */
.how{left:0;top:1302px;width:1200px;height:436px;background:linear-gradient(100deg,#e8a7b5 0%,#dd5c7b 35%,#d9385f 65%,#c9455e 100%)}
.how-title{top:1350px;color:var(--white)}
.how-text{left:150px;width:900px;top:1428px;font-size:18px;line-height:30px;color:var(--white);text-align:center}
.btn-ghost{left:490px;top:1600px;width:217px;height:52px;line-height:50px;border:1.5px solid rgba(255,255,255,.8);color:var(--white);font-family:"Montserrat",sans-serif;font-size:19px;text-align:center}

/* blog */
.blog-title{top:1760px;color:var(--ink)}
.post{width:483px}
.post-photo{width:483px;height:207px}
.post h4{margin-top:24px;font-family:"Montserrat",sans-serif;font-weight:400;font-size:19px;line-height:24px;letter-spacing:.3px;color:var(--ink)}
.post p{margin-top:10px;font-size:15px;line-height:22px;color:var(--light)}
.btn-solid{display:inline-block;margin-top:26px;width:127px;height:41px;line-height:41px;background:var(--red);color:var(--white);font-size:15px;text-align:center}

/* locations */
.locations{left:0;top:2350px;width:1200px;height:407px;background:linear-gradient(180deg,#ef9ea7 0%,#e7a59d 45%,#c98a89 75%,#a87680 100%)}
.loc-title{top:2384px;color:var(--white)}
.loc-sub{left:0;width:1200px;top:2448px;font-size:17px;color:var(--white);text-align:center}
.field{top:2531px;width:236px;height:38px;border:1px solid rgba(255,255,255,.75);padding-left:16px;line-height:36px;font-size:14px;color:rgba(255,255,255,.9)}
.send{left:521px;top:2607px;width:158px;height:41px;line-height:41px;background:var(--red);color:var(--white);font-family:"Montserrat",sans-serif;font-size:16px;text-align:center}

/* work with us */
.work-title{top:2790px;color:var(--ink)}
.work-text{left:148px;width:904px;top:2858px;font-size:14.5px;line-height:29px;color:var(--muted);text-align:center}
.work-text p+p{margin-top:16px}
.work-btn{left:490px;top:3143px;width:217px;height:50px;line-height:48px;font-size:19px}

/* footer */
.footer{left:0;top:3243px;width:1200px;height:328px;background:var(--red)}
.f-col{top:3288px}
.f-col h5{font-family:"Montserrat",sans-serif;font-weight:600;font-size:16px;letter-spacing:.5px;color:var(--white)}
.f-col ul{list-style:none;margin-top:18px}
.f-col li{font-size:14px;line-height:30px;color:#fde6eb}
.f-col li svg{vertical-align:-2px;margin-right:12px}
.f-divider{top:3288px;width:1px;height:170px;background:rgba(255,255,255,.35)}
.f-rule{left:102px;top:3500px;width:1000px;height:1px;background:rgba(255,255,255,.4)}
.f-copy{left:102px;top:3522px;font-size:13px;color:#fde6eb}
.socials{margin-top:16px;display:flex;gap:6px}
.socials span{width:36px;height:36px;border-radius:50%;background:#f6f6f6;border:2px solid rgba(255,255,255,.6)}
</style>
</head>
<body>

<header class="abs hero">
  <div class="hero-photo" role="img" aria-label="Photo of a red semi truck driving on a highway between green rocky hills"></div>
  <svg class="hero-curve" width="1200" height="120" viewBox="0 0 1200 120"><path d="M0 60 Q600 -30 1200 60 L1200 120 L0 120 Z" fill="#fff"/></svg>
</header>
<div class="abs brand">TOLBRIX</div>
<h1 class="abs hero-title">ROADSIDE ASSISTANCE IN THE USA</h1>
<p class="abs hero-sub">Getting you back on the road fast anywhere in USA, whether you need a quick jump, lock out services, or towing.</p>
<svg class="abs play" width="72" height="72" viewBox="0 0 72 72" aria-label="Play video"><circle cx="36" cy="36" r="33" fill="rgba(255,255,255,.15)" stroke="#fff" stroke-width="3"/><path d="M29 23 L50 36 L29 49 Z" fill="none" stroke="#fff" stroke-width="3" stroke-linejoin="round"/></svg>

<h2 class="abs section-title about-title">About Us</h2>
<p class="abs about-text">Tolbrix offers on demand roadside assistance to heavy trucks and 18 wheelers anywhere in the USA. Driving ng, your time is money. We understand how important it is for you to get reliable roadside services fast, and Tolbrix provides quick service and facilitates safe, cashless payments. Our innovative approach to roadside assistance means that you get back on the road quicker, without having to pay expensive subscriptions to a traditional roadside assistance service.</p>

<div class="abs feature" style="left:85px;top:928px">
  <svg width="136" height="136" viewBox="0 0 136 136"><circle cx="68" cy="68" r="66" fill="var(--red)"/><circle cx="68" cy="68" r="58" fill="none" stroke="#fff" stroke-width="2"/><path d="M44 72 A25 25 0 1 0 52 49" fill="none" stroke="#fff" stroke-width="5" stroke-linecap="round"/><path d="M44 40 L52 49 L41 53" fill="none" stroke="#fff" stroke-width="5" stroke-linecap="round" stroke-linejoin="round"/><path d="M68 54 V70 L79 78" fill="none" stroke="#fff" stroke-width="5" stroke-linecap="round"/></svg>
  <h3>QUICK SERVICE</h3>
  <p>Our app can be downloaded on either any phone or tablet and service is available any where in the United States.</p>
  <a class="btn-outline">READ MORE</a>
</div>
<div class="abs feature" style="left:440px;top:928px">
  <svg width="136" height="136" viewBox="0 0 136 136"><circle cx="68" cy="68" r="66" fill="var(--red)"/><circle cx="68" cy="68" r="58" fill="none" stroke="#fff" stroke-width="2"/><rect x="34" y="50" width="40" height="30" fill="#fff"/><path d="M78 58 H92 L102 70 V80 H78 Z" fill="#fff"/><circle cx="48" cy="86" r="7" fill="#fff" stroke="var(--red)" stroke-width="3"/><circle cx="90" cy="86" r="7" fill="#fff" stroke="var(--red)" stroke-width="3"/></svg>
  <h3>FACILITATES SAFE</h3>
  <p>Our app can be downloaded on either any phone or tablet and service is available any where in the United States.</p>
  <a class="btn-outline">READ MORE</a>
</div>
<div class="abs feature" style="left:792px;top:928px">
  <svg width="136" height="136" viewBox="0 0 136 136"><circle cx="68" cy="68" r="66" fill="var(--red)"/><circle cx="68" cy="68" r="58" fill="none" stroke="#fff" stroke-width="2"/><rect x="40" y="50" width="56" height="36" rx="4" fill="#fff"/><rect x="40" y="58" width="56" height="7" fill="var(--red)"/><rect x="46" y="73" width="16" height="5" fill="var(--red)"/></svg>
  <h3>CASHLESS PAYMENTS</h3>
  <p>Our app can be downloaded on either any phone or tablet and service is available any where in the United States.</p>
  <a class="btn-outline">READ MORE</a>
</div>

<section class="abs how" role="img" aria-label="Photo of a truck wheel and roadside repair under a red overlay"></section>
<h2 class="abs section-title how-title">How it works</h2>
<div class="abs how-text">
  <p>Register with Tolbrix to gain access to our services. In the event of an emergency, connect to roadside assistance instantly with our app.</p>
  <p style="margin-top:22px">Service providers respond to your needs in real time, getting you back on the road fast.</p>
</div>
<a class="abs btn-ghost">READ MORE</a>

<h2 class="abs section-title blog-title">Latest <span class="accent">Blog</span></h2>
<article class="abs post" style="left:102px;top:1860px">
  <div class="post-photo" role="img" aria-label="Photo of a driver stretching beside a red truck" style="background:linear-gradient(120deg,#7fae5c 0%,#d52a35 40%,#b01d28 70%,#9bb3c4 100%)"></div>
  <h4>EXERCISES/YOGA FOR TRUCK DRIVERS TO STAY FIT.</h4>
  <p>The blog topics should be focused on general well being of truckers, new places to explore, best truckstops, how to handle an emergency etc.</p>
  <a class="btn-solid">Read More ›</a>
</article>
<article class="abs post" style="left:619px;top:1860px">
  <div class="post-photo" role="img" aria-label="Photo of a person on the phone beside a car with its hood open" style="background:linear-gradient(120deg,#4c4f58 0%,#6c7c9c 40%,#9ea3ad 70%,#3b3f47 100%)"></div>
  <h4>10 BEST TRUCKSTOPS IN TEXAS TO UNWIND YOUR DAY.</h4>
  <p>The blog topics should be focused on general well being of truckers, new places to explore, best truckstops, how to handle an emergency etc.</p>
  <a class="btn-solid">Read More ›</a>
</article>

<section class="abs locations" role="img" aria-label="Photo of a city skyline at sunset under a pink overlay"></section>
<h2 class="abs section-title loc-title">Locations Covered</h2>
<p class="abs loc-sub">Cover entire states of USA</p>
<div class="abs field" style="left:102px">Enter Your Name</div>
<div class="abs field" style="left:357px">Your Email Address</div>
<div class="abs field" style="left:612px">Your Phone Number</div>
<div class="abs field" style="left:864px">Subject</div>
<a class="abs send">SEND NOW</a>

<h2 class="abs section-title work-title">Work With Us</h2>
<div class="abs work-text">
  <p>Tolbrix is the most efficient way to find roadside work and get paid, hassle-free, cash-free and in real time. Our easy to use app gives you the tools and support to bring your roadside assistance business to the next level, whether you have one driver or ten. Managing teams has never been easier with Tolbrix. During registration, you select the services that your team can manage and Tolbrix will match you with people in need, so you can get to work. Setting up our app is easy and our service providers can get started the same day in most cases.</p>
  <p>Sick of tedious and time-consuming claim forms? Skip them! Tolbrix handles the paperwork so you can focus on what you do best. Tolbrix takes the place of dispatcher, getting your roadside assistance vehicles on the road where they belong, and where they can make more money for your business!</p>
</div>
<a class="abs btn-outline work-btn">READ MORE</a>

<footer class="abs footer"></footer>
<div class="abs f-col" style="left:102px"><h5>COMPANY</h5><ul><li>Home</li><li>About Us</li><li>How it works</li><li>Blog</li><li>Servicer Login</li></ul></div>
<div class="abs f-divider" style="left:234px"></div>
<div class="abs f-col" style="left:276px"><h5>SERVICES</h5><ul><li>Quick Service</li><li>Facilitates Safe</li><li>Cashless Payments</li><li>Others</li></ul></div>
<div class="abs f-divider" style="left:458px"></div>
<div class="abs f-col" style="left:498px"><h5>GET IN TOUCH</h5><ul>
  <li><svg width="14" height="14" viewBox="0 0 14 14"><path d="M3 1 L5.5 1 L6.5 4.5 L5 5.8 Q6.5 8.5 8.2 9 L9.5 7.5 L13 8.5 L13 11 Q12 13 9.5 12.5 Q2 10 1.5 3.5 Q1.5 1.5 3 1 Z" fill="#fff"/></svg>Call us on 555-014-2387</li>
  <li><svg width="14" height="14" viewBox="0 0 14 14"><rect x="1" y="3" width="12" height="9" fill="#fff"/><path d="M1 3 L7 8 L13 3" fill="none" stroke="var(--red)" stroke-width="1.3"/></svg>hello@tolbrixmail.net</li>
</ul></div>
<div class="abs f-divider" style="left:728px"></div>
<div class="abs f-col" style="left:769px"><h5>WHY US</h5><ul><li>Customers</li><li>Team</li><li>FAQ</li><li>Contact</li></ul></div>
<div class="abs f-divider" style="left:886px"></div>
<div class="abs f-col" style="left:926px"><h5>FOLLLOW US</h5><ul><li>Please connect with us on</li></ul>
  <div class="socials" aria-label="Social network links"><span></span><span></span><span></span><span></span></div>
</div>
<div class="abs f-rule"></div>
<p class="abs f-copy">© 2016 Company Name. All right reserved. Term of Use</p>

</body>
</html>
```